Flyer for photo scanning business

Hello,
I need a flyer created for my business that would be suitable for print, to drop in letterboxes in my local community.

I would like the flyer to convey very simply the services I offer which is scanning negatives, slides and VHS tapes to digital files.
Hopefully it can make it look like an easy process, as people are often daunted by the task of sorting through old photos so they don't always get around to having them scanned.

I have a pinned facebook post that can be used by the designer to reference my services. Pricing does not need to be included on the flyer.
http://facebook.com/brightvaleimaging

Target Market(s)

Parents & Grandparents

Requirements
Must have
• Must make my services look simple! Refer to pinned facebook post for detailed outline of my services.

I would like to flyer to point towards my contact details -
www.brightvale.com
Margot 0478 219 836

Colours in line with my logo/brand (uploaded to brief).
Nice to have
• Stock images of 35mm film negatives, 8mm film, VHS tapes, or Lumavert slides would be worth including. I have also uploaded a mockup of the USB sticks that I provide with digitised images.
Should not have
• no prices needed,

```html
<!DOCTYPE html>
<html lang="en">
<head>
<meta charset="utf-8">
<title>Brightvale Digital Flyer</title>
<link href="https://fonts.googleapis.com/css2?family=Montserrat:wght@400;600;700;800&family=Great+Vibes&display=swap" rel="stylesheet">
<style>
  :root{
    --bg:#e9e6df;
    --navy:#16233f;
    --navy-deep:#0f1a31;
    --blue:#3f7fc1;
    --blue-mid:#5b95d0;
    --blue-light:#9cc0e6;
    --ice:#dfeaf6;
    --white:#ffffff;
    --black:#111418;
  }
  *{box-sizing:border-box;margin:0;padding:0}
  html,body{width:1200px;height:2380px;overflow:hidden;background:var(--bg)}
  body{font-family:"Montserrat",Arial,sans-serif;position:relative}
  .flyer{position:absolute;left:50px;top:412px;width:1100px;height:1556px;background:var(--white);overflow:hidden;box-shadow:0 10px 30px rgba(0,0,0,.15)}
  .photo{position:absolute}
  .photo--film{left:0;top:0;width:390px;height:300px;background:linear-gradient(135deg,#5a2b22,#2a1a17 60%,#8a5a3a)}
  .photo--child{left:0;top:300px;width:560px;height:620px;background:linear-gradient(160deg,#b27c5e,#7c3a35 55%,#2f3d6e)}
  .photo--slides{right:0;top:0;width:390px;height:300px;background:linear-gradient(200deg,#e8c7a0,#b37c55 55%,#5c3d2e)}
  .photo--wedding{right:0;top:300px;width:540px;height:620px;background:linear-gradient(180deg,#c9ccd0,#7f8790 50%,#e8e6e2)}
  .brand-panel{position:absolute;left:380px;top:0;width:340px;height:300px;background:var(--navy-deep);display:flex;flex-direction:column;align-items:center;justify-content:center;gap:14px}
  .brand-mark{width:64px;height:64px;border:3px solid var(--blue-light);border-radius:50%}
  .brand-name{font-weight:600;color:var(--white);font-size:30px;letter-spacing:5px;text-align:center;line-height:1.3}
  .brand-name span{display:block;font-size:17px;letter-spacing:6px;color:var(--blue-light)}
  .heart{position:absolute;left:270px;top:260px;width:560px;height:500px}
  .headline{position:absolute;left:330px;top:345px;width:440px;text-align:center;color:var(--white);font-weight:700;font-size:40px;line-height:1.25;letter-spacing:1px}
  .headline .accent{color:var(--blue-light)}
  .services-bg{position:absolute;left:0;top:760px;width:1100px;height:720px}
  .usb{position:absolute;left:340px;top:770px;width:420px;height:110px;border-radius:16px;background:linear-gradient(90deg,#d9dde2,#9aa4ae 50%,#cfd6de)}
  .services-label{position:absolute;left:0;width:100%;top:912px;text-align:center;color:var(--ice);font-size:18px;letter-spacing:5px;font-weight:600}
  .services-label::before,.services-label::after{content:"";display:inline-block;width:90px;height:2px;background:var(--ice);vertical-align:middle;margin:0 18px}
  .service{position:absolute;top:990px;width:440px;color:var(--white);text-align:center}
  .service--scan{left:80px}
  .service--video{right:80px}
  .service h2{font-size:36px;font-weight:800;line-height:1.1}
  .service h3{font-size:32px;font-weight:400;color:var(--ice);letter-spacing:1px;margin-bottom:22px}
  .service p{font-size:22px;line-height:1.45;font-weight:600}
  .service .small{font-size:16px;font-weight:400;margin-top:20px;color:var(--ice)}
  .divider{position:absolute;left:549px;top:1000px;width:2px;height:330px;background:rgba(255,255,255,.4)}
  .contact-bar{position:absolute;left:0;bottom:0;width:100%;height:96px;background:var(--black);display:flex;align-items:center;justify-content:space-between;padding:0 50px;color:var(--white)}
  .contact-person{display:flex;align-items:center;gap:18px}
  .contact-name{font-family:"Great Vibes",cursive;font-size:44px}
  .phone-icon{width:38px;height:38px}
  .contact-phone,.contact-web{font-size:32px;font-weight:700;letter-spacing:1px}
</style>
</head>
<body>
<div class="flyer">
  <div class="photo photo--film" role="img" aria-label="Strips of 35mm film negatives and a film camera"></div>
  <div class="photo photo--slides" role="img" aria-label="Old film slides and reels"></div>
  <div class="photo photo--child" role="img" aria-label="Vintage family photo of a young child in a red hat"></div>
  <div class="photo photo--wedding" role="img" aria-label="Vintage wedding photo of a bride and groom"></div>

  <div class="brand-panel">
    <div class="brand-mark"></div>
    <div class="brand-name">BRIGHTVALE<span>DIGITAL</span></div>
  </div>

  <svg class="heart" viewBox="0 0 560 500" aria-hidden="true">
    <path d="M280 490 C70 345 6 240 6 145 C6 60 70 8 150 8 C212 8 258 45 280 92 C302 45 348 8 410 8 C490 8 554 60 554 145 C554 240 490 345 280 490Z" fill="var(--navy-deep)" stroke="var(--blue-mid)" stroke-width="10"/>
  </svg>
  <h1 class="headline">KEEP YOUR<br><span class="accent">PRECIOUS<br>MEMORIES</span><br>FOREVER</h1>

  <svg class="services-bg" viewBox="0 0 1100 720" preserveAspectRatio="none" aria-hidden="true">
    <defs>
      <linearGradient id="svcGrad" x1="0" y1="0" x2="0" y2="1">
        <stop offset="0" stop-color="#5b95d0"/>
        <stop offset="1" stop-color="#2e66a6"/>
      </linearGradient>
    </defs>
    <path d="M0 40 Q550 220 1100 40 L1100 720 L0 720Z" fill="var(--blue-light)"/>
    <path d="M0 70 Q550 250 1100 70 L1100 720 L0 720Z" fill="url(#svcGrad)"/>
  </svg>

  <div class="usb" role="img" aria-label="Branded USB sticks supplied with digitised files"></div>

  <div class="services-label">OUR SERVICES</div>

  <div class="service service--scan">
    <h2>PHOTO NEGATIVE</h2>
    <h3>SCANNING</h3>
    <p>Digitising photo slides and negatives into high resolution files.</p>
    <p class="small">Prints and albums also welcome, sorted and returned safely to you.</p>
  </div>
  <div class="divider"></div>
  <div class="service service--video">
    <h2>SLIDES AND VHS</h2>
    <h3>DIGITISING</h3>
    <p>Conversion of VHS tapes to computer friendly video files using high quality broadcast equipment.</p>
    <p class="small">Files delivered on a branded USB stick ready to share.</p>
  </div>

  <div class="contact-bar">
    <div class="contact-person">
      <span class="contact-name">Margot</span>
      <svg class="phone-icon" viewBox="0 0 40 40" aria-hidden="true">
        <circle cx="20" cy="20" r="19" fill="var(--blue)"/>
        <path d="M14 10 l4 0 l2 6 l-3 2 q2 5 7 7 l2 -3 l6 2 l0 4 q-1 3 -4 3 q-10 -1 -16 -12 q-2 -5 2 -9z" fill="var(--white)"/>
      </svg>
      <span class="contact-phone">0478 219 836</span>
    </div>
    <span class="contact-web">www.brightvale.com</span>
  </div>
</div>
</body>
</html>
```